Logo integration into existing html template for a local sports club (handball)

We have a fresh installed joomla, a template and a vector logo. The vector logo should now be integrated into the template.

```html
<!DOCTYPE html>
<html lang="de">
<head>
<meta charset="utf-8">
<title>Handball Club Seewald</title>
<link rel="stylesheet" href="https://fonts.googleapis.com/css2?family=Noto+Serif:ital,wght@0,400;1,400&family=Poiret+One&display=swap">
<style>
  :root {
    --top-bar: #1b1b1b;
    --header-bg: #2a2a2a;
    --header-dark: #1f1f1f;
    --brand-red: #d8141c;
    --nav-top: #ffffff;
    --nav-bottom: #ececec;
    --nav-line: #d6d6d6;
    --nav-text: #333333;
    --link-blue: #2a78c2;
    --page-bg: #f4f4f4;
    --panel-bg: #ffffff;
    --text-grey: #555555;
    --muted: #9a9a9a;
    --caption-bg: #050505;
  }
  * { box-sizing: border-box; margin: 0; padding: 0; }
  html, body { width: 1200px; height: 765px; overflow: hidden; }
  body { position: relative; background: var(--page-bg); font-family: Arial, Helvetica, sans-serif; color: var(--text-grey); }

  .top-bar { position: absolute; left: 0; top: 0; width: 1200px; height: 36px; background: var(--top-bar); }
  .top-bar .webmaster { position: absolute; right: 12px; top: 13px; font-size: 12px; color: var(--muted); }

  .site-header { position: absolute; left: 0; top: 36px; width: 1200px; height: 205px;
    background: linear-gradient(180deg, var(--header-bg), var(--header-dark)); }
  .brand { position: absolute; left: 18px; top: 58px; display: flex; align-items: center; gap: 12px; }
  .brand-mark { width: 44px; height: 44px; background: var(--brand-red); }
  .brand-name { font-family: Arial, Helvetica, sans-serif; font-weight: bold; font-size: 20px; color: #ffffff; line-height: 1.1; }

  .search { position: absolute; left: 617px; top: 72px; width: 568px; height: 40px; background: #1c1c1c;
    border: 1px solid #3a3a3a; border-radius: 4px; }
  .search .placeholder { position: absolute; left: 14px; top: 13px; font-size: 12px; color: #8a8a8a; }
  .search .button { position: absolute; right: 3px; top: 3px; width: 78px; height: 32px; background: #ffffff;
    border-radius: 3px; font-size: 11px; font-weight: bold; color: #222; text-align: center; line-height: 32px; }

  .main-nav { position: absolute; left: 10px; top: 147px; width: 1178px; height: 93px;
    background: linear-gradient(180deg, var(--nav-top), var(--nav-bottom)); border-radius: 3px 3px 0 0; }
  .nav-item { position: absolute; top: 0; height: 93px; }
  .nav-item .title { position: absolute; top: 20px; font-size: 15px; font-weight: bold; color: var(--nav-text); white-space: nowrap; }
  .nav-item .sub { position: absolute; top: 53px; font-size: 12px; color: #555; white-space: nowrap; }
  .nav-item.home .title { top: 37px; font-size: 15px; color: var(--link-blue); }
  .nav-sep { position: absolute; top: 35px; width: 1px; height: 28px; background: var(--nav-line); }
  .nav-chev { position: absolute; top: 36px; }

  .slider { position: absolute; left: 10px; top: 240px; width: 1178px; height: 190px;
    background: linear-gradient(90deg, #c9c2b8 0%, #e3dfd8 30%, #d9cfa8 55%, #c9b56a 75%, #8f8e92 100%); }
  .pager { position: absolute; left: 23px; top: 22px; display: flex; gap: 8px; }
  .pager span { width: 28px; height: 22px; background: rgba(30,30,30,.85); color: #fff; font-size: 11px; text-align: center; line-height: 22px; }
  .pager span.active { background: var(--brand-red); }
  .slider-arrow { position: absolute; top: 88px; width: 46px; height: 46px; background: rgba(0,0,0,.55); border-radius: 3px; }
  .slider-arrow.prev { left: 50px; }
  .slider-arrow.next { right: 40px; }
  .slide-caption { position: absolute; left: 10px; top: 430px; width: 1178px; height: 46px; background: var(--caption-bg);
    font-family: "Poiret One", sans-serif; font-size: 26px; color: #fff; padding: 8px 14px; }

  .content { position: absolute; left: 10px; top: 476px; width: 707px; height: 289px; }
  .post-title { position: absolute; left: 9px; font-family: "Noto Serif", serif; font-size: 22px; color: var(--link-blue); white-space: nowrap; }
  .like-button { position: absolute; left: 25px; top: 95px; height: 22px; padding: 0 7px; display: flex; align-items: center; gap: 5px;
    border: 1px solid #c6cfe0; border-radius: 3px; background: #eef1f7; font-size: 11px; color: #3b5998; }
  .like-button i { width: 12px; height: 12px; background: #3b5998; display: block; }
  .post-text { position: absolute; left: 143px; width: 550px; font-size: 13px; line-height: 20px; color: var(--text-grey); text-align: justify; }

  .sidebar { position: absolute; top: 476px; height: 289px; }
  .season { left: 718px; width: 235px; border-left: 1px solid #e2e2e2; }
  .login { left: 953px; width: 235px; border-left: 1px solid #e2e2e2; background: #f7f7f7; }
  .panel-head { position: absolute; left: 0; top: 17px; width: 100%; height: 57px; background: var(--panel-bg);
    font-family: "Noto Serif", serif; font-style: italic; font-size: 22px; color: #555; padding: 14px 28px; box-shadow: 0 1px 3px rgba(0,0,0,.08); }
  .season .label { position: absolute; left: 28px; top: 98px; font-size: 13px; color: #444; }
  .season ul { position: absolute; left: 28px; top: 117px; list-style: none; }
  .season li { font-size: 13px; line-height: 21px; color: var(--link-blue); display: flex; align-items: center; gap: 9px; }
  .season li::before { content: ""; border-left: 5px solid #333; border-top: 4px solid transparent; border-bottom: 4px solid transparent; }
  .login .field-label { position: absolute; left: 40px; font-size: 13px; color: #333; }
  .login .field { position: absolute; left: 41px; width: 168px; height: 23px; background: #fff; border: 1px solid #bdbdbd; }
</style>
</head>
<body>
  <div class="top-bar"><span class="webmaster">Webmaster</span></div>

  <header class="site-header">
    <div class="brand">
      <span class="brand-mark"></span>
      <span class="brand-name">Handball Club<br>Seewald</span>
    </div>
    <div class="search">
      <span class="placeholder">Suchen...</span>
      <span class="button">SUCHEN</span>
    </div>
  </header>

  <nav class="main-nav">
    <div class="nav-item home" style="left:39px"><span class="title">Home</span></div>
    <svg class="nav-chev" style="left:124px" width="10" height="10" viewBox="0 0 10 10"><path d="M2 2l3 3 3-3M2 5l3 3 3-3" stroke="#666" fill="none"/></svg>
    <div class="nav-item" style="left:147px"><span class="title">Mannschaften</span><span class="sub">Teams Des HCSs</span></div>
    <span class="nav-sep" style="left:292px"></span>
    <svg class="nav-chev" style="left:297px" width="10" height="10" viewBox="0 0 10 10"><path d="M2 2l3 3 3-3M2 5l3 3 3-3" stroke="#666" fill="none"/></svg>
    <div class="nav-item" style="left:317px"><span class="title">Verein</span><span class="sub">Gemeinsam Stark</span></div>
    <span class="nav-sep" style="left:456px"></span>
    <svg class="nav-chev" style="left:461px" width="10" height="10" viewBox="0 0 10 10"><path d="M2 2l3 3 3-3M2 5l3 3 3-3" stroke="#666" fill="none"/></svg>
    <div class="nav-item" style="left:481px"><span class="title">Berichte</span><span class="sub">Top Aktuell</span></div>
    <span class="nav-sep" style="left:585px"></span>
    <svg class="nav-chev" style="left:590px" width="10" height="10" viewBox="0 0 10 10"><path d="M2 2l3 3 3-3M2 5l3 3 3-3" stroke="#666" fill="none"/></svg>
    <div class="nav-item" style="left:611px"><span class="title">Verschiedenes</span><span class="sub">Rund Um Den HCS</span></div>
    <span class="nav-sep" style="left:750px"></span>
    <div class="nav-item" style="left:783px"><span class="title">Sponsoren</span><span class="sub">Unsere Gönner</span></div>
    <span class="nav-sep" style="left:902px"></span>
    <div class="nav-item" style="left:935px"><span class="title">Intern</span><span class="sub">Community</span></div>
    <span class="nav-sep" style="left:1030px"></span>
  </nav>

  <section class="slider" role="img" aria-label="Foto: Spielszene eines Handballspiels vor dem Tor">
    <div class="pager"><span>1</span><span>2</span><span class="active">3</span><span>4</span></div>
    <svg class="slider-arrow prev" viewBox="0 0 46 46"><path d="M27 13l-10 10 10 10" stroke="#fff" stroke-width="4" fill="none"/></svg>
    <svg class="slider-arrow next" viewBox="0 0 46 46"><path d="M19 13l10 10-10 10" stroke="#fff" stroke-width="4" fill="none"/></svg>
  </section>
  <div class="slide-caption">Herren 1</div>

  <main class="content">
    <h2 class="post-title" style="top:20px">HC Seewald am Uferwiesen-Plausch!!</h2>
    <div class="like-button"><i></i>Gefällt mir</div>
    <p class="post-text" style="top:80px">Eines vorweg. Es sind alle Vereinsmitglieder unverletzt und (wieder) auf den Beinen. Es war ein absolut toller Event. Schade, dass dieser Anlass nur alle zwei Jahre stattfindet. Der HCS wird sicher auch in zwei Jahren wieder Ehre einlegen...</p>
    <h2 class="post-title" style="top:210px">Herren 1: Nationaler Cup-Gegner zugelost!</h2>
    <p class="post-text" style="top:279px">In der ersten Runde des Cups startet der HC Seewald mit einem Heimspiel. Gegner</p>
  </main>

  <aside class="sidebar season">
    <div class="panel-head">Aktuelle Saison</div>
    <span class="label">Rangliste:</span>
    <ul><li>Herren 1</li><li>Herren 2</li></ul>
  </aside>

  <aside class="sidebar login">
    <div class="panel-head">Login</div>
    <span class="field-label" style="top:140px">Benutzername</span>
    <span class="field" style="top:157px"></span>
    <span class="field-label" style="top:222px">Passwort</span>
    <span class="field" style="top:239px"></span>
  </aside>
</body>
</html>
```